Business Card Design

We need a business card design for a consulting firm which provides safety and risk management consulting services for public venues, hotels and tourist attractions. The business card design should include the attached logo unedited with a design based on incorporating the existing logo with a design of geometric patterns or lines on a predominantly white background.

Industry/Entity Type

Business

Contact Information for Business Card

Dane Morvello
Director & Principal Consultant

Ph: +61 (0) 468502 174
PO Box 456 Kellmore Vale, NSW Australia 2563
info@corvanwellandcare.com

(back of card to include website www.corvanwellandcare.com

```html
<!DOCTYPE html>
<html lang="en">
<head>
<meta charset="utf-8">
<title>Corvan Well &amp; Care – Business Cards</title>
<link href="https://fonts.googleapis.com/css2?family=Lato:wght@400;700;900&display=swap" rel="stylesheet">
<style>
  :root {
    --blue: #1e8fcc;
    --green: #6cb544;
    --ink: #1d1d1d;
    --grey: #6a6a6a;
    --paper: #ffffff;
    --backdrop: #e4e6e8;
    --divider: #9ab8cc;
  }
  * { box-sizing: border-box; margin: 0; padding: 0; }
  html, body { width: 1200px; height: 926px; overflow: hidden; }
  body {
    background: var(--backdrop);
    font-family: "Lato", Arial, sans-serif;
    color: var(--ink);
    position: relative;
  }
  .card {
    position: absolute;
    left: 240px;
    width: 720px;
    height: 411px;
    background: var(--paper);
    box-shadow: 0 6px 18px rgba(0,0,0,0.18);
    overflow: hidden;
  }
  .card--back { top: 36px; }
  .card--front { top: 479px; }

  .brand {
    position: absolute;
    display: flex;
    align-items: center;
    gap: 12px;
  }
  .brand__mark {
    width: 34px; height: 34px;
    background: var(--green);
  }
  .brand__name {
    font-weight: 900;
    font-size: 38px;
    letter-spacing: 0.5px;
    color: var(--blue);
    text-transform: uppercase;
    white-space: nowrap;
  }

  .card--back .brand { left: 0; right: 0; top: 148px; justify-content: center; }
  .card--back .website {
    position: absolute; left: 0; right: 0; top: 228px;
    text-align: center;
    font-size: 17px; font-weight: 700;
    letter-spacing: 4px;
    color: var(--grey);
  }
  .corner { position: absolute; top: 0; right: 0; }

  .card--front .brand { left: 180px; top: 46px; }
  .card--front .brand__name { font-size: 30px; }
  .card--front .brand__mark { width: 28px; height: 28px; }

  .person {
    position: absolute; left: 130px; top: 134px;
    text-align: right;
    width: 218px;
  }
  .person__name {
    font-weight: 900; font-size: 22px;
    color: var(--blue);
    text-transform: uppercase;
    letter-spacing: 0.3px;
  }
  .person__title { font-size: 14px; margin-top: 2px; }
  .contact-divider {
    position: absolute; left: 364px; top: 136px;
    width: 1px; height: 64px;
    background: var(--divider);
  }
  .contact {
    position: absolute; left: 378px; top: 138px;
    list-style: none;
    font-size: 17px;
  }
  .contact li { display: flex; align-items: center; gap: 9px; height: 28px; }
  .contact svg { width: 14px; height: 14px; fill: var(--green); flex: none; }

  .swoosh { position: absolute; left: 0; top: 0; }
  .address {
    position: absolute; left: 26px; bottom: 22px;
    color: var(--paper);
    font-size: 16px;
  }
</style>
</head>
<body>

<section class="card card--back" aria-label="Card back">
  <svg class="corner" width="120" height="70" viewBox="0 0 120 70">
    <polygon points="0,0 120,0 120,70" fill="var(--blue)"/>
  </svg>
  <div class="brand">
    <span class="brand__mark"></span>
    <span class="brand__name">Corvan Well &amp; Care</span>
  </div>
  <p class="website">www.corvanwellandcare.com</p>
</section>

<section class="card card--front" aria-label="Card front">
  <svg class="swoosh" width="720" height="411" viewBox="0 0 720 411">
    <path d="M0,240 C190,236 390,300 580,392 C420,318 210,272 0,272 Z" fill="var(--green)"/>
    <path d="M0,286 C230,288 440,352 540,411 L0,411 Z" fill="var(--blue)"/>
    <path d="M450,411 L720,330 L720,411 Z" fill="var(--paper)"/>
    <path d="M478,411 L720,340 L720,411 Z" fill="var(--green)"/>
  </svg>

  <div class="brand">
    <span class="brand__mark"></span>
    <span class="brand__name">Corvan Well &amp; Care</span>
  </div>

  <div class="person">
    <h1 class="person__name">Dane Morvello</h1>
    <p class="person__title">Director &amp; Principal Consultant</p>
  </div>
  <span class="contact-divider"></span>
  <ul class="contact">
    <li>
      <svg viewBox="0 0 24 24" aria-hidden="true"><path d="M6.6 10.8a15 15 0 0 0 6.6 6.6l2.2-2.2c.3-.3.7-.4 1-.2 1.1.4 2.3.6 3.6.6.6 0 1 .4 1 1V20c0 .6-.4 1-1 1A17 17 0 0 1 3 4c0-.6.4-1 1-1h3.5c.6 0 1 .4 1 1 0 1.3.2 2.5.6 3.6.1.3 0 .7-.2 1z"/></svg>
      <span>+61 (0) 468502 174</span>
    </li>
    <li>
      <svg viewBox="0 0 24 24" aria-hidden="true"><path d="M2 5h20v14H2z M3 6l9 7 9-7" /><path d="M3.5 6.5 12 13l8.5-6.5" fill="none" stroke="#fff" stroke-width="1.6"/></svg>
      <span>info@corvanwellandcare.com</span>
    </li>
  </ul>

  <p class="address">PO Box 456 Kellmore Vale, NSW Australia 2563</p>
</section>

</body>
</html>
```